Music Web page

We are the largest community of artists, bands, podcasters and creators of music. We need web pages design.

What we need:
1. Registration form page
- Full Name
- Username
- Email Address
- Password
- Captcha

2. Songs/Artists gallery page
- Cover
- Simple MP3 Player
- Share | Like | Comments

3. Contact us page
- Name
- Email
- Phone
- Message
- Captcha

Send me a registration form first, If it makes me "hands on the air" , then I will continue to work with you.

Industry/Entity Type

Artists

Colors
eb1f27

Requirements
Nice to have
• Dark / black color for background

```html
<!DOCTYPE html>
<html lang="en">
<head>
<meta charset="utf-8">
<title>Create a Free Account – Amphall</title>
<link href="https://fonts.googleapis.com/css2?family=Open+Sans:wght@400;600;700&display=swap" rel="stylesheet">
<style>
  :root {
    --page-black: #000000;
    --header-line: #1c1c1c;
    --panel-bg: rgba(24, 24, 24, 0.92);
    --panel-head: rgba(40, 40, 40, 0.6);
    --panel-border: #333333;
    --field-border: #3b3b3b;
    --field-text: #6e6e6e;
    --tick-bg: #050505;
    --tick-icon: #4a4a4a;
    --heading: #8a8a8a;
    --body-text: #a8a8a8;
    --logo-light: #c8c8c8;
    --accent-blue: #0080e0;
    --white: #ffffff;
  }
  * { box-sizing: border-box; margin: 0; padding: 0; }
  html, body { width: 1200px; height: 1000px; overflow: hidden; background: var(--white); }
  body { font-family: "Open Sans", sans-serif; position: relative; }

  .site-header {
    position: absolute; left: 0; top: 0; width: 1200px; height: 128px;
    background: var(--page-black); border-bottom: 1px solid var(--header-line);
  }
  .brand {
    position: absolute; left: 88px; top: 38px;
    font-size: 40px; font-weight: 700; letter-spacing: 1px; color: var(--logo-light);
    line-height: 52px;
  }
  .login-tab {
    position: absolute; left: 1000px; top: 0; width: 137px; height: 42px;
    background: #161616; border: 1px solid #333; border-top: none; border-radius: 0 0 4px 4px;
    display: flex; align-items: center; color: #d0d0d0; font-size: 16px;
  }
  .login-tab .lock { width: 52px; display: flex; justify-content: center; border-right: 1px solid #333; height: 22px; align-items: center; }
  .login-tab span { padding-left: 15px; }

  .hero {
    position: absolute; left: 0; top: 129px; width: 1200px; height: 699px;
    background: var(--page-black); overflow: hidden;
  }
  .hero-photo {
    position: absolute; left: 440px; top: 0; width: 760px; height: 699px;
    background:
      radial-gradient(ellipse at 55% 35%, rgba(150,150,150,0.55) 0%, rgba(70,70,70,0.35) 35%, rgba(0,0,0,0) 70%),
      linear-gradient(120deg, #000 0%, #1a1a1a 45%, #2a2a2a 70%, #0a0a0a 100%);
  }

  .intro { position: absolute; left: 88px; top: 60px; width: 380px; }
  .intro h1 { font-size: 26px; font-weight: 400; color: var(--heading); line-height: 36px; }
  .intro p { margin-top: 14px; font-size: 12px; color: var(--body-text); line-height: 15px; }

  .signup-panel {
    position: absolute; left: 88px; top: 162px; width: 388px; height: 491px;
    background: var(--panel-bg); border: 1px solid var(--panel-border); border-radius: 4px;
  }
  .signup-panel .panel-title {
    height: 56px; background: var(--panel-head); border-radius: 4px 4px 0 0;
    padding-left: 35px; font-size: 19px; color: #bdbdbd; line-height: 56px;
  }
  .field {
    position: absolute; left: 35px; width: 312px; height: 49px;
    border: 1px solid var(--field-border); border-radius: 4px;
    font-size: 12px; color: var(--field-text); padding-left: 22px; line-height: 47px;
  }
  .field .tick {
    position: absolute; right: 10px; top: 7px; width: 33px; height: 33px;
    background: var(--tick-bg); border-radius: 4px; display: flex; align-items: center; justify-content: center;
  }
  .field .captcha-code { position: absolute; left: 114px; top: 0; font-size: 24px; color: #555; }

  .agree { position: absolute; left: 35px; top: 376px; display: flex; align-items: center; font-size: 12px; color: #777; }
  .agree .box { width: 18px; height: 17px; border: 1px solid #444; border-radius: 3px; margin-right: 13px; }

  .create-btn {
    position: absolute; left: 35px; top: 413px; width: 177px; height: 49px;
    background: linear-gradient(#3d3d3d, #1c1c1c); border: 1px solid #4a4a4a; border-radius: 4px;
    color: #c4c4c4; font-weight: 700; font-size: 15px; text-align: center; line-height: 46px;
    font-family: "Open Sans", sans-serif;
  }

  .site-footer {
    position: absolute; left: 0; top: 828px; width: 1200px; height: 79px; background: var(--accent-blue);
  }
  .site-footer p {
    position: absolute; right: 63px; top: 36px; font-family: Arial, sans-serif; font-size: 11px; color: var(--white);
  }
</style>
</head>
<body>
  <header class="site-header">
    <div class="brand">AMPHALL</div>
    <div class="login-tab">
      <div class="lock">
        <svg width="12" height="14" viewBox="0 0 12 14"><path d="M3 6V4a3 3 0 0 1 6 0v2" fill="none" stroke="#777" stroke-width="1.8"/><rect x="1" y="6" width="10" height="8" rx="1" fill="#777"/></svg>
      </div>
      <span>LOGIN</span>
    </div>
  </header>

  <main class="hero">
    <div class="hero-photo" role="img" aria-label="Dark close-up photograph of an electric guitar body, pickups and strings"></div>

    <section class="intro">
      <h1>Create a Free Account!</h1>
      <p>Lorem iopsum dolor sit amit,consetetur sadipscing eliter,sed diam voluptua. At vero eso et accusam et justo duo dolores et ea rebum.</p>
    </section>

    <form class="signup-panel">
      <div class="panel-title">New Account</div>
      <div class="field" style="top:67px">Full Name<span class="tick"><svg width="14" height="11" viewBox="0 0 14 11"><path d="M1 6l4 4 8-9" fill="none" stroke="var(--tick-icon)" stroke-width="1.6"/></svg></span></div>
      <div class="field" style="top:126px">Username<span class="tick"><svg width="14" height="11" viewBox="0 0 14 11"><path d="M1 6l4 4 8-9" fill="none" stroke="var(--tick-icon)" stroke-width="1.6"/></svg></span></div>
      <div class="field" style="top:185px">Email Address<span class="tick"><svg width="14" height="11" viewBox="0 0 14 11"><path d="M1 6l4 4 8-9" fill="none" stroke="var(--tick-icon)" stroke-width="1.6"/></svg></span></div>
      <div class="field" style="top:245px">Password<span class="tick"><svg width="14" height="11" viewBox="0 0 14 11"><path d="M1 6l4 4 8-9" fill="none" stroke="var(--tick-icon)" stroke-width="1.6"/></svg></span></div>
      <div class="field" style="top:304px">Captcha<span class="captcha-code">QwR35</span><span class="tick"><svg width="18" height="12" viewBox="0 0 18 12"><path d="M6 2H3a2 2 0 0 0-2 2v3a2 2 0 0 0 2 2h3M12 3h3a2 2 0 0 1 2 2v3a2 2 0 0 1-2 2H8M10 8l-2 2 2 2" fill="none" stroke="#5a5a5a" stroke-width="1.6"/></svg></span></div>
      <label class="agree"><span class="box"></span>I Agree to terms and condition.</label>
      <button type="button" class="create-btn">Create Account</button>
    </form>
  </main>

  <footer class="site-footer">
    <p>Copyright © 2014 Company Name. All Rights Reserved.</p>
  </footer>
</body>
</html>
```